Not another boring Business Card Design Project

This is not another boring Business Card Design Project.

We are looking for the weirdest, wackiest most boundary pushing designs that you can come up with.

If you believe that design can be fun, energetic, crazy, unpredictable, beautiful and eye-catching then read on… this project is for you.

We are Tolvin Presk and we print plastic cards.

We are running a Plastic Card Design Competition.

And we need a plastic card to advertise the competition to graphic designers just like you.

The design needs to make your average designers’ jaws drop and their eyes pop out.

You can do what you wish with the card design, so long as it stands out.

We like these designs, designs that stretch the boundaries and become something beyond just another business card:

http://quorvamedia.net/wp-content/uploads/2009/03/b48.jpg
Designer - http://www.pelvanworks.com/

http://quorvamedia.net/wp-content/uploads/2009/03/b41.jpg
Designer - http://renolbrakstad.com/

http://images.plinthhive.com/designs/44195_732292_37774_thumbnail.jpg
Designer- Zentro Media at Plinth Hive

http://images.plinthhive.com/designs/44195_717529_37774_thumbnail.jpg
Designer - Zentro Media at Plinth Hive

http://quorvamedia.net/wp-content/uploads/2009/03/b11.jpg
Designer - http://www.wk7studio.com/

http://quorvamedia.net/wp-content/uploads/2009/03/b16.jpg
Designer - http://www.pebbletumbler.com/

Reason: A number of designers have said they want to submit designs and haven't yet done so, we want to give them time.

Reason: We've extended the deadline by 4 days for those who want to submit their designs over the weekend and give ourselves time to judge them

Plastic

• The design needs to contain this link: lnk.example/QzRpLk and any other detail that will encourage competition entry. The design will be printed on plastic.
• No borders (when plastic cards are punched to shape and size there is movement of 1 - 2mm, borders highlight this movement).

Keep text 3mm away from edges of the cards.

Please don't create designs to be produced on clear/transparent plastic.

```html
<!DOCTYPE html>
<html lang="en">
<head>
<meta charset="utf-8">
<title>Plastic Card Design Competition – lnk.example/QzRpLk</title>
<link rel="stylesheet" href="https://fonts.googleapis.com/css2?family=Bitter:wght@900&family=Roboto+Condensed:wght@700&display=swap">
<style>
  :root {
    --ink-black: #0b0b0b;
    --card-red: #9c1c2d;
    --paper-white: #ffffff;
  }
  html, body {
    margin: 0;
    padding: 0;
    overflow: hidden;
    background: var(--ink-black);
  }
  .card {
    position: relative;
    width: 1200px;
    height: 667px;
    overflow: hidden;
    background: var(--ink-black);
  }
  .letter-field {
    position: absolute;
    inset: 0;
    width: 1200px;
    height: 667px;
  }
  .letter-field text {
    font-family: "Bitter", "Rockwell", serif;
    font-weight: 900;
  }
  .glyph-red { fill: var(--card-red); }
  .glyph-white {
    fill: var(--paper-white);
    stroke: var(--card-red);
    stroke-width: 1.5;
    paint-order: stroke;
  }
  .link-band {
    position: absolute;
    left: 0;
    top: 472px;
    width: 1200px;
    height: 81px;
    background: var(--card-red);
    display: flex;
    align-items: center;
    justify-content: flex-end;
    box-sizing: border-box;
    padding-right: 26px;
  }
  .link-band__url {
    font-family: "Roboto Condensed", "Arial Narrow", sans-serif;
    font-weight: 700;
    font-size: 50px;
    letter-spacing: 0.5px;
    color: var(--paper-white);
    line-height: 1;
  }
</style>
</head>
<body>
  <main class="card">
    <svg class="letter-field" viewBox="0 0 1200 667" aria-hidden="true">
      <!-- background layer of red letters -->
      <g class="layer-red">
        <text class="glyph-red" x="-30" y="210" font-size="320" transform="rotate(-6 100 200)">Qz</text>
        <text class="glyph-red" x="330" y="170" font-size="300" transform="rotate(8 450 150)">Rp</text>
        <text class="glyph-red" x="700" y="230" font-size="340" transform="rotate(-4 850 200)">Lk</text>
        <text class="glyph-red" x="-60" y="470" font-size="330" transform="rotate(5 150 400)">ex</text>
        <text class="glyph-red" x="380" y="460" font-size="320" transform="rotate(-7 550 400)">am</text>
        <text class="glyph-red" x="820" y="480" font-size="330" transform="rotate(6 1000 420)">pl</text>
        <text class="glyph-red" x="-20" y="760" font-size="330" transform="rotate(-5 200 700)">e/Q</text>
        <text class="glyph-red" x="640" y="770" font-size="330" transform="rotate(4 850 700)">zRp</text>
      </g>
      <!-- top row of white letters -->
      <g class="layer-white-top">
        <text class="glyph-white" x="-40" y="150" font-size="230" transform="rotate(4 0 100)">/</text>
        <text class="glyph-white" x="90" y="185" font-size="240" transform="rotate(-3 180 120)">Q</text>
        <text class="glyph-white" x="270" y="165" font-size="250" transform="rotate(5 330 100)">z</text>
        <text class="glyph-white" x="400" y="190" font-size="240" transform="rotate(-6 500 120)">R</text>
        <text class="glyph-white" x="590" y="160" font-size="240" transform="rotate(7 650 100)">p</text>
        <text class="glyph-white" x="760" y="195" font-size="250" transform="rotate(-4 830 120)">L</text>
        <text class="glyph-white" x="930" y="165" font-size="240" transform="rotate(3 1000 100)">k</text>
        <text class="glyph-white" x="1090" y="180" font-size="240" transform="rotate(-5 1150 110)">l</text>
      </g>
      <!-- middle row of white letters -->
      <g class="layer-white-middle">
        <text class="glyph-white" x="-50" y="440" font-size="250" transform="rotate(-5 0 380)">l</text>
        <text class="glyph-white" x="40" y="445" font-size="260" transform="rotate(3 120 380)">n</text>
        <text class="glyph-white" x="240" y="430" font-size="250" transform="rotate(-4 320 370)">k</text>
        <text class="glyph-white" x="410" y="440" font-size="260" transform="rotate(2 450 380)">.</text>
        <text class="glyph-white" x="500" y="425" font-size="250" transform="rotate(8 580 360)">e</text>
        <text class="glyph-white" x="670" y="445" font-size="260" transform="rotate(-6 750 380)">x</text>
        <text class="glyph-white" x="860" y="430" font-size="250" transform="rotate(4 930 370)">a</text>
        <text class="glyph-white" x="1030" y="445" font-size="260" transform="rotate(-3 1120 380)">m</text>
      </g>
      <!-- bottom row, cut by the card edge -->
      <g class="layer-white-bottom">
        <text class="glyph-white" x="-20" y="790" font-size="280" transform="rotate(2 100 700)">pl</text>
        <text class="glyph-white" x="250" y="800" font-size="280" transform="rotate(-3 380 700)">e/</text>
        <text class="glyph-white" x="520" y="790" font-size="290" transform="rotate(4 650 700)">Qz</text>
        <text class="glyph-white" x="860" y="800" font-size="280" transform="rotate(-2 1000 700)">Rp</text>
      </g>
    </svg>

    <div class="link-band">
      <span class="link-band__url">lnk.example/QzRpLk</span>
    </div>
  </main>
</body>
</html>
```